2 page Web Site Design (Coded), simple, not picky

I need a web portal for a PPC marketing business. I have the logo, some imagery, and some websites to base the design on.

***Background***
The name of the business is "Quiet Harbor Outreach Advisors" or QHOA. We provide listings in a searchable database for Dental Sleep Medicine doctors. These are doctors who treat snoring/sleep apnea/and CPAP users with oral appliances. Client doctors will have their own "landing page website" where PPC prospects land from the PPC campaigns. Logos for supporting/landing page websites have been uploaded.
***End Background***

THIS website (for you to design) is to introduce doctors to the concept and detail the services. i.e. PPC campaign management services, listing on a national database of Dental Sleep Medicine practitioners, and a fully featured website dedicated to Snoring, Sleep Apnea, and CPAP Alternative treatment (those websites are "Farewell-Rumble.com", "Farewell-NightGasp.com", and ""Farewell-MaskTube.com")

SEM websites whose look I enjoy are:

http://www.brindlequay.com/marketing-services/pay-per-click/

http://www.orchardvantage.com/welcome/pay-per-click-services/

http://www.lanternpeak.com/marketing-services/paid-search-management/

The main colors are Red, White, & Blue. Red and blue used mostly for accents/emphasis.

The main/index page's purpose is to, as best possible, convey the idea of SEM campaign management with supporting websites being their best option for internet marketing!
The secondary page is just a slightly modified layout where details can be explained.

Target Market(s)

Dentists who practice Dental Sleep Medicine (see www.rqtvo.org)

Industry/Entity Type

Marketing

Requirements
Must have
• -Sign-up form for the generation of leads... Simple script that sends E-mail is fine... Doctor's Name, Business Name, Business Address, E-mail address, phone #.

-Graphics that will clearly describe the services being provided.

```html
<!DOCTYPE html>
<html lang="en">
<head>
<meta charset="utf-8">
<title>QHOA – Quiet Harbor Outreach Advisors</title>
<link href="https://fonts.googleapis.com/css2?family=PT+Sans:ital,wght@0,400;0,700;1,400&family=Dosis:wght@300;400&display=swap" rel="stylesheet">
<style>
:root{
  --red:#c8161d;
  --red-dark:#a50f16;
  --blue:#1f4f9e;
  --blue-dark:#153a7a;
  --text:#333;
  --muted:#6b6b6b;
  --line:#d9d9d9;
  --panel:#f4f6fa;
  --footer:#efefef;
  --icon:#2b5aa4;
  --icon-grey:#a9a9a9;
}
*{box-sizing:border-box;margin:0;padding:0}
html,body{width:885px;height:1200px;overflow:hidden}
body{position:relative;background:#fff;font-family:"PT Sans",Arial,sans-serif;color:var(--text)}
.abs{position:absolute}

.top-rule{left:0;top:0;width:885px;height:4px;background:var(--red)}
.site-header{left:0;top:4px;width:885px;height:110px;background:linear-gradient(#fff,#f6f6f6)}
.brand{left:22px;top:22px;display:flex;align-items:center;gap:8px}
.brand-dot{width:42px;height:42px;border-radius:50%;background:var(--blue)}
.brand-name{font-size:34px;font-weight:700;color:var(--red);line-height:1}
.brand-tag{left:22px;top:74px;font-size:10.5px;font-weight:700;color:var(--red);letter-spacing:.2px}
.social{display:flex;gap:8px}
.social span{width:24px;height:24px;border-radius:50%;background:var(--icon);display:block}
.social.head{left:750px;top:30px}
.callus{right:21px;top:68px;font-size:18px;color:var(--red)}

.main-nav{left:0;top:114px;width:885px;height:46px;background:linear-gradient(#d8232a,#b5121a);border-top:1px solid #e45a5f;display:flex;align-items:center;padding-left:18px}
.main-nav a{color:#fff;font-size:12px;font-weight:700;text-decoration:none;padding:0 20px;border-left:1px solid rgba(255,255,255,.55);line-height:18px}
.main-nav a:first-child{border-left:none}

.hero{left:0;top:160px;width:885px;height:270px;background:linear-gradient(90deg,#a9c8e6 0%,#c7dcef 35%,#dfe9f1 52%,#d9b8a1 62%,#cfa384 78%,#b9a79b 100%)}
.hero-box{left:23px;top:200px;width:427px;height:161px;background:rgba(255,255,255,.45)}
.hero-title{left:50px;top:222px;font-family:"Dosis",sans-serif;font-weight:300;font-size:28px;line-height:28px;color:var(--blue-dark)}
.hero-sub{left:54px;top:284px;font-family:"Dosis",sans-serif;font-size:17px;color:var(--blue-dark)}
.btn-more{left:55px;top:315px;width:75px;height:22px;background:var(--blue-dark);color:#fff;font-family:"Dosis",sans-serif;font-size:12px;text-align:center;line-height:22px;border-radius:2px}

.content{left:22px;top:452px;width:562px}
.content h1{font-size:16.5px;font-weight:400;color:var(--red);margin-bottom:5px}
.lead{font-size:11px;color:#222;margin-bottom:3px}
.body-copy{font-size:9.5px;line-height:15.5px;color:var(--muted);text-align:justify}
.body-copy+.body-copy{margin-top:20px}
.divider{left:22px;top:670px;width:562px;height:1px;background:var(--line)}
.services-head{left:22px;top:687px;font-size:14px;font-weight:400;color:#222}
.services-sub{left:22px;top:706px;font-size:9.5px;font-style:italic;color:#444}
.photo{border:1px solid #ddd}
.ph-sleeper{left:21px;top:728px;width:192px;height:101px;background:linear-gradient(120deg,#6f93bd,#a9bfd6 55%,#e9e9ee)}
.feature-text{left:223px;top:727px;width:361px}
.feature-text .big{font-size:11px;line-height:16px;color:#444;text-align:justify;margin-bottom:3px}
.feature-wrap{left:22px;top:838px;width:562px}
.card{width:244px}
.card .photo{height:102px}
.card h3{font-size:11px;font-weight:400;color:#222;margin:13px 0 5px 3px}
.card p{font-size:9.5px;line-height:15.7px;color:var(--muted);text-align:justify;padding:0 3px}
.card-a{left:21px;top:884px}
.card-b{left:292px;top:884px}
.ph-clinic{background:linear-gradient(90deg,#dfe7ee,#f4f7f9 50%,#b9cfe0)}
.ph-rest{background:linear-gradient(90deg,#d9d3cf,#8a6856 45%,#e8e3e0)}

.panel{background:#fff;border:1px solid #e2e5ea;border-radius:3px}
.contact{left:603px;top:450px;width:259px;height:295px;overflow:hidden}
.contact-head{height:41px;background:linear-gradient(#2d62b4,#1f4f9e);color:#fff;font-size:14px;padding:13px 0 0 16px}
.field{position:absolute;left:14px;font-size:9.5px;color:#333}
.input{position:absolute;left:96px;width:148px;height:19px;border:1px solid #ccc;background:#fff}
.btn{position:absolute;top:247px;height:22px;color:#fff;font-size:11px;text-align:center;line-height:22px;border-radius:2px}
.btn-submit{left:96px;width:63px;background:var(--blue)}
.btn-reset{left:164px;width:59px;background:var(--red)}

.blog{left:603px;top:752px;width:259px;height:334px}
.blog-head{height:40px;background:var(--panel);color:var(--blue);font-size:15px;padding:10px 0 0 17px}
.post{position:absolute;left:17px;width:232px}
.post h4{font-size:11.5px;font-weight:400;font-style:italic;color:var(--red);margin-bottom:3px;white-space:nowrap}
.post p{font-size:9px;line-height:15.5px;font-style:italic;color:var(--muted)}
.post time{display:block;font-size:9.5px;font-weight:700;color:#333;margin-top:2px}

.site-footer{left:0;top:1101px;width:885px;height:99px;background:var(--footer)}
.foot-nav{left:22px;top:1120px;display:flex;gap:15px;font-size:9.5px;color:#333}
.copyright{left:22px;top:1143px;font-size:9.5px;color:#555}
.social.foot{left:758px;top:1119px;gap:5px}
.social.foot span{width:20px;height:20px;background:var(--icon-grey)}
</style>
</head>
<body>
<div class="abs top-rule"></div>
<header class="abs site-header"></header>
<div class="abs brand"><span class="brand-dot"></span><span class="brand-name">QHOA</span></div>
<div class="abs brand-tag">Quiet Harbor Outreach Advisors</div>
<div class="abs social head"><span></span><span></span><span></span><span></span></div>
<div class="abs callus">Call us &nbsp;+1800 555 0142</div>

<nav class="abs main-nav">
  <a>Home</a><a>About Company</a><a>Services</a><a>Testimonials</a><a>Blog</a><a>News</a><a>Information</a><a>Contact</a>
</nav>

<section class="abs hero" role="img" aria-label="Photo of a smiling older couple against a soft blue sky"></section>
<div class="abs hero-box"></div>
<div class="abs hero-title">We Are Quiet Harbor<br>Outreach Advisors</div>
<div class="abs hero-sub">Lorem ipsum dolor sit amet, adipiscing elit.</div>
<div class="abs btn-more">learn more</div>

<main class="abs content">
  <h1>Welcome to Quiet Harbor Outreach Advisors</h1>
  <p class="lead">Lorem ipsum dolor sit amet, consectetuer adipiscing elit. Nam cursus.</p>
  <p class="body-copy">Morbi ut mi. Nullam enim leo, egestas id, condimentum at, laoreet mattis, massa. Sed eleifend nonummy diam. Praesent mauris ante, elementum et, bibendum at, posuere sit amet, nibh. Duis tincidunt lectus quis dui viverra vestibulum. Suspendisse vulputate aliquam dui. Nulla elementum dui ut augue. Aliquam vehicula mi at mauris. Maecenas placerat, nisl at consequat rhoncus, sem nunc gravida justo, quis eleifend arcu velit quis lacus. Morbi magna magna, tincidunt a, mattis non, imperdiet vitae, tellus. Sed odio est, auctor ac, sollicitudin in, consequat vitae, orci. Fusce id felis. Vivamus sollicitudin metus eget eros.</p>
  <p class="body-copy">Pellentesque habitant morbi tristique senectus et netus et malesuada fames ac turpis egestas. In posuere felis nec tortor. Pellentesque faucibus. Ut accumsan ultricies elit. Maecenas at justo id velit placerat molestie. Donec dictum lectus non odio. Cras a ante vitae enim iaculis aliquam. Mauris nunc quam, venenatis nec</p>
</main>
<div class="abs divider"></div>
<h2 class="abs services-head">Services &amp; Our Therapy</h2>
<p class="abs services-sub">Lorem ipsum dolor sit amet, consectetuer adipiscing elit. Nam cursus.</p>
<div class="abs photo ph-sleeper" role="img" aria-label="Photo of a man sleeping peacefully on a white pillow"></div>
<div class="abs feature-text">
  <p class="big">Morbi ut mi. Nullam enim leo, egestas id, condimentum at, laoreet mattis, massa. Sed eleifend nonummy diam.</p>
  <p class="body-copy" style="margin-bottom:3px">Praesent mauris ante, elementum et, bibendum at, posuere sit amet, nibh.</p>
  <p class="body-copy" style="margin-top:0">Duis tincidunt lectus quis dui viverra vestibulum. Suspendisse vulputate aliquam dui. Nulla elementum dui ut augue. Aliquam vehicula mi at mauris. Maecenas placerat, nisl at consequat rhoncus, sem nunc gravida justo, quis eleifend arcu velit</p>
</div>
<p class="abs body-copy feature-wrap">quis lacus. Morbi magna magna, tincidunt a, mattis non, imperdiet vitae, tellus. Sed odio est, auctor ac, sollicitudin in, consequat vitae, orci. Fusce id felis. Vivamus sollicitudin metus eget eros.</p>

<article class="abs card card-a">
  <div class="photo ph-clinic" role="img" aria-label="Photo of a doctor with medical staff in a bright clinic"></div>
  <h3>Sleeping Consultancy Tittle here</h3>
  <p>Morbi magna magna, tincidunt a, mattis non, imperdiet vitae, tellus. Sed odio est, auctor ac, sollicitudin in, consequat vitae, orci. Fusce id felis. Vivamus sollicitudin metus eget eros.</p>
</article>
<article class="abs card card-b">
  <div class="photo ph-rest" role="img" aria-label="Photo of a woman resting her head on a white pillow"></div>
  <h3>Sleeping Consultancy Tittle here</h3>
  <p>Morbi magna magna, tincidunt a, mattis non, imperdiet vitae, tellus. Sed odio est, auctor ac, sollicitudin in, consequat vitae, orci. Fusce id felis. Vivamus sollicitudin metus eget eros.</p>
</article>

<aside class="abs panel contact">
  <div class="contact-head">Contact Info Form</div>
  <label class="field" style="top:65px">Doctor's Name:</label><span class="input" style="top:63px"></span>
  <label class="field" style="top:91px">Business Name:</label><span class="input" style="top:89px"></span>
  <label class="field" style="top:118px">Email Add:</label><span class="input" style="top:116px"></span>
  <label class="field" style="top:148px">Phone no:</label><span class="input" style="top:146px"></span>
  <label class="field" style="top:176px">Address:</label><span class="input" style="top:168px;height:70px"></span>
  <span class="btn btn-submit">SUBMIT</span><span class="btn btn-reset">RESET</span>
</aside>

<aside class="abs panel blog">
  <div class="blog-head">Recent Blog Post</div>
  <div class="post" style="top:51px">
    <h4>Duis tincidunt lectus quis dui viverra bulum.</h4>
    <p>Suspendisse vulputate aliquam dui. Nulla elementum dui ut augue. Aliquam vehicula</p>
    <time>3 hours ago</time>
  </div>
  <div class="post" style="top:135px">
    <h4>Ut ante enim, dapibus malesuada, fringilla</h4>
    <p>Suspendisse vulputate aliquam dui. Nulla elementum dui ut augue. Aliquam vehicula</p>
    <time>3 hours ago</time>
  </div>
  <div class="post" style="top:216px;left:19px">
    <h4>Phasellus felis dolor scelerisque tempus eget</h4>
    <p>Proin dui lectus, cursus eu, mattis laoreet, viverra sit amet, quam. Curabitur vel dolor ultrices ipsum dictum tristique. Praesent vitae lacus. Ut velit enim, vestibulum non, fermentum nec</p>
    <time>8 hours ago</time>
  </div>
</aside>

<footer class="abs site-footer"></footer>
<nav class="abs foot-nav"><span>Home</span><span>About Company</span><span>Services</span><span>Testimonials</span><span>Blog</span><span>News</span><span>Information</span><span>Contact</span></nav>
<div class="abs copyright">Copyright © 2012 Company Name &nbsp;|&nbsp; Privacy Policy</div>
<div class="abs social foot"><span></span><span></span><span></span><span></span></div>
</body>
</html>
```